A private security company called "Tavrin Security Services Ltd"

Hello everybody,

We need a web page for a company based in NZ. It is mainly an informative website so it would be wonderful if the designer puts their absolute best into making it a website that I would really appreciate. The website needs to show professionalism and also needs to make our web surfers find the information they need in a click. the company's colour is black and silver, and if those two colours could be integrated into the website it would be absolutely lovely. Please do contact me for any information.

Sincerely,
Dorian Velasko

Industry/Entity Type

Security

```html
<!DOCTYPE html>
<html lang="en">
<head>
<meta charset="utf-8">
<title>Tavrin Security Services Ltd</title>
<link href="https://fonts.googleapis.com/css2?family=Questrial&family=Open+Sans:wght@400;600&display=swap" rel="stylesheet">
<style>
:root{
  --ink:#1a1a1a;
  --muted:#8a8a8a;
  --body:#5a5a5a;
  --blue:#1f4fa0;
  --sky:#2a9be0;
  --navy:#1c3f8a;
  --silver-top:#e6e6e6;
  --silver-bot:#c4c4c4;
  --rule:#d6d6d6;
  --footer:#000;
  --footer-bar:#0d0d0d;
  --footer-text:#e8e8e8;
}
*{margin:0;padding:0;box-sizing:border-box}
html,body{width:914px;height:1200px;overflow:hidden;background:#fff}
body{position:relative;font-family:"Open Sans",sans-serif;color:var(--body)}
.abs{position:absolute}
.brand{left:80px;top:30px;display:flex;align-items:center;gap:10px}
.brand-mark{width:36px;height:36px;border-radius:50%;background:var(--ink)}
.brand-name{font-family:"Questrial",sans-serif;font-size:17px;color:var(--ink);letter-spacing:.5px;line-height:1.1;width:190px}
.hotline{right:78px;top:41px;text-align:right;font-family:"Questrial",sans-serif}
.hotline .label{color:var(--blue);font-size:14px}
.hotline .phone{color:#444;font-size:18px;margin-top:1px}
.main-nav{left:74px;top:94px;width:766px;height:40px;display:flex;border:1px solid #b5b5b5;background:linear-gradient(var(--silver-top),var(--silver-bot))}
.main-nav a{font-family:"Questrial",sans-serif;font-size:12.5px;color:var(--ink);text-decoration:none;display:flex;align-items:center;justify-content:center;border-right:1px solid #a8a8a8}
.main-nav a:last-child{border-right:0}
.hero{left:74px;top:134px;width:766px;height:306px;background:linear-gradient(115deg,#8fa3bb 0%,#cfccc6 40%,#a9a6a2 70%,#b3b5b8 100%)}
.hero-caption{left:74px;top:260px;width:374px;height:88px;background:rgba(20,20,20,.82);padding:16px 0 0 30px;font-family:"Questrial",sans-serif}
.hero-caption .t1{color:var(--sky);font-size:25px;line-height:1.1}
.hero-caption .t2{color:#fff;font-size:19px;margin-top:5px}
.dots{left:433px;top:421px;display:flex;gap:3px}
.dots span{width:10px;height:10px;border-radius:50%;background:#fff}
.card{top:464px;width:182px}
.card .thumb{height:86px}
.card h3{font-family:"Questrial",sans-serif;font-weight:400;color:var(--navy);font-size:14.5px;margin-top:10px}
.card p{font-size:9.2px;line-height:16px;color:var(--muted);margin-top:4px}
.card .btn{display:inline-block;margin-top:7px;width:93px;height:27px;line-height:27px;text-align:center;color:#fff;font-size:9.6px;border-radius:3px;background:linear-gradient(#4a4a4a,#1e1e1e);text-decoration:none}
.divider{left:74px;top:678px;width:766px;height:1px;background:var(--rule)}
.welcome{left:75px;top:727px;width:470px}
.welcome h1{font-family:"Questrial",sans-serif;font-weight:400;font-size:19px;color:var(--ink)}
.welcome .lead{font-size:11px;line-height:17px;color:#666;margin-top:9px;padding-left:3px}
.welcome p{font-size:9.3px;line-height:16.5px;color:#666;margin-top:8px;padding-left:3px}
.video{left:576px;top:726px;width:263px;height:174px;border:1px solid #cfcfcf;background:linear-gradient(#9fbcd8 0%,#b8cfe2 45%,#8a9c62 70%,#6f8048 100%)}
.play{left:693px;top:791px}
.footer{left:0;top:963px;width:914px;height:183px;background:var(--footer)}
.footer-col{top:996px}
.footer-col h4{font-family:"Questrial",sans-serif;font-weight:400;color:#fff;font-size:14px;margin-bottom:7px}
.footer-col li{list-style:none;font-size:9.6px;color:var(--footer-text);line-height:18.7px;padding-left:2px}
.footer-bar{left:0;top:1146px;width:914px;height:54px;background:var(--footer-bar);border-top:1px solid #1c1c1c}
.copyright{left:79px;top:1164px;font-size:9.4px;color:#9a9a9a}
.social{left:743px;top:1162px;display:flex;gap:5px}
.social span{width:16px;height:16px;border-radius:2px}
</style>
</head>
<body>

<header>
  <div class="abs brand">
    <span class="brand-mark"></span>
    <span class="brand-name">Tavrin Security Services Ltd</span>
  </div>
  <div class="abs hotline">
    <div class="label">24/ Operation</div>
    <div class="phone">864.3120.4471</div>
  </div>
  <nav class="abs main-nav">
    <a style="width:84px">HOME</a>
    <a style="width:105px">ABOUT US</a>
    <a style="width:97px">SERVICES</a>
    <a style="width:152px">SECURITY GUARDS</a>
    <a style="width:92px">ALARMS</a>
    <a style="width:98px">SUPPORT</a>
    <a style="width:138px">CONTACT US</a>
  </nav>
</header>

<section>
  <div class="abs hero" role="img" aria-label="Security guard in uniform climbing past a modern glass building"></div>
  <div class="abs hero-caption">
    <div class="t1">SECURITY SERVICES</div>
    <div class="t2">ALIQUAM ERAT PURUS CURSUS</div>
  </div>
  <div class="abs dots"><span></span><span></span><span></span><span></span></div>
</section>

<section>
  <div class="abs card" style="left:74px">
    <div class="thumb" role="img" aria-label="Uniformed security guards standing in a row" style="background:#6f7f98"></div>
    <h3>Security Guarding</h3>
    <p>Pellentesque faucibus Ut accumsan ultricies elit Maecenas at justo</p>
    <a class="btn">READ MORE</a>
  </div>
  <div class="abs card" style="left:269px">
    <div class="thumb" role="img" aria-label="Hand pressing an alarm keypad" style="background:#e2e2e0"></div>
    <h3>Security Cam &amp; Alarms</h3>
    <p>Pellentesque faucibus Ut accumsan ultricies elit Maecenas at justo</p>
    <a class="btn">READ MORE</a>
  </div>
  <div class="abs card" style="left:463px">
    <div class="thumb" role="img" aria-label="Security camera overlooking a harbour" style="background:#6f98bf"></div>
    <h3>Security Cameras</h3>
    <p>Pellentesque faucibus Ut accumsan ultricies elit Maecenas at justo</p>
    <a class="btn">READ MORE</a>
  </div>
  <div class="abs card" style="left:658px">
    <div class="thumb" role="img" aria-label="Personal security officer holding a baton" style="background:#34363d"></div>
    <h3>Personal Security</h3>
    <p>Pellentesque faucibus Ut accumsan ultricies elit Maecenas at justo</p>
    <a class="btn">READ MORE</a>
  </div>
</section>

<div class="abs divider"></div>

<section class="abs welcome">
  <h1>WELCOME TO TAVRIN SECURITY SERVICES</h1>
  <p class="lead">Tavrin Security is a New Zealand based company with a single objective - to excel in the protection of people, property and assets.</p>
  <p>We provide a high level of security services using the most experienced officers at a reasonable and fair price. We believe in using a risk-based approach to every aspect of site protection to provide our clients with the most cost effective solutions.</p>
  <p>We strongly believe that we are in business with our clients. Each thing we do must be measured against our clients' safety objectives. At the end of the day our client's security is our success.</p>
</section>
<div class="abs video" role="img" aria-label="Video: security officer with radio in an open field"></div>
<svg class="abs play" width="32" height="32" viewBox="0 0 32 32">
  <circle cx="16" cy="16" r="14" fill="rgba(0,0,0,.55)" stroke="#fff" stroke-width="2"/>
  <path d="M13 10 L22 16 L13 22 Z" fill="#fff"/>
</svg>

<footer>
  <div class="abs footer"></div>
  <div class="abs footer-col" style="left:80px">
    <h4>COMPANY</h4>
    <ul><li>About Us</li><li>Services</li><li>Solutions</li><li>Case Studies</li><li>Awards</li></ul>
  </div>
  <div class="abs footer-col" style="left:224px">
    <h4>FEATURES</h4>
    <ul><li>Sed porta</li><li>Suspendisse quam</li><li>Leo molestie</li><li>Sed luctus quis</li><li>Tempor cursus</li></ul>
  </div>
  <div class="abs footer-col" style="left:381px">
    <h4>SERVICES</h4>
    <ul><li>Phasellus felis dolor</li><li>Scelerisque tempus</li><li>Eget lobortis</li><li>Libero Aliquam</li></ul>
  </div>
  <div class="abs footer-col" style="left:539px">
    <h4>SUPPORT</h4>
    <ul><li>Sed porta</li><li>Suspendisse quam</li><li>Leo molestie</li><li>Sed luctus quis</li></ul>
  </div>
  <div class="abs footer-col" style="left:681px">
    <h4>CONTACT</h4>
    <ul><li>48 Orrin Lane, Suite 12</li><li>Wellford, Harlow 4021 NZ</li><li>Tel: +64 (0)9 555 0148</li><li>hello@tavrinsecure.example</li></ul>
  </div>
  <div class="abs footer-bar"></div>
  <div class="abs copyright">© 2014 Company Name.&nbsp; All right reserved.&nbsp; Term of Use</div>
  <div class="abs social">
    <span style="background:#3b5998"></span>
    <span style="background:#29a9e1"></span>
    <span style="background:#0e76a8"></span>
    <span style="background:#f26522"></span>
  </div>
</footer>

</body>
</html>
```